Lumen Cove Skincare - Package Design

New Beauty label needing product packaging design. Looking for elegant and stylish design to represent our premium brand.

This project is for 1 label and 1 box design. The winning designer will be assigned another project for the next product in the range. (to be paid as a new project)

This product is for "Dead Sea Mud Mask". Please see the label format and jar attached. Please note there are 2 different jars we are considering (will have a mud inside). Please feel free to choose whichever one suits your design best.

The labels and boxes are to retain the product information, such as size, ingredients etc, but is to be updated to our brand. You can move or display the other information as you wish.

the size of the dead sea mud mask color box is 72*72*85mm (length*width*height)
the size of dead sea mud mask label is 218*58mm (width*height)

Target Market(s)

Women 15 to 65

Requirements
Must have
• Must be elegant and represent our brand which is a premium beauty product.
Should not have
• Dark blue. Dark purple etc. Colours should compliment the logo

```html
<!DOCTYPE html>
<html lang="en">
<head>
<meta charset="utf-8">
<title>Lumen Cove Skincare – Dead Sea Mud Mask Packaging</title>
<link rel="stylesheet" href="https://fonts.googleapis.com/css2?family=Josefin+Sans:wght@300;400;600&family=Kalam:wght@300&family=Arimo:wght@400;700&display=swap">
<style>
  :root {
    --stage: #e9e9e9;
    --texture-gold: #a3966a;
    --texture-light: #ecebe6;
    --panel-black: #1f1d1c;
    --gold: #c9a23a;
    --gold-light: #e6c55a;
    --ink-light: #f4f2ee;
    --ink-soft: #d8d5cf;
    --ink-dark: #1a1a1a;
  }
  * { box-sizing: border-box; margin: 0; padding: 0; }
  html, body { width: 1200px; height: 803px; overflow: hidden; }
  body { background: var(--stage); position: relative; font-family: "Josefin Sans", sans-serif; }

  .pack {
    position: absolute;
    background: var(--texture-light);
    overflow: hidden;
  }
  .pack--label { left: 290px; top: 308px; width: 238px; height: 252px; font-size: 8px; }
  .pack--box   { left: 628px; top: 234px; width: 274px; height: 332px; font-size: 10px; }

  .pack__texture {
    position: absolute; inset: 0;
    background: linear-gradient(90deg,
      var(--texture-gold) 0%, var(--texture-light) 18%, #c8bf9f 34%,
      var(--texture-light) 52%, #bdb38c 70%, var(--texture-light) 86%, var(--texture-gold) 100%);
    opacity: .85;
  }

  .brand-banner {
    position: absolute; left: 50%; transform: translateX(-50%);
    top: 0; width: 15.6em; height: 11.6em;
    background: var(--panel-black);
    clip-path: polygon(0 0, 100% 0, 100% 76%, 50% 100%, 0 76%);
    display: flex; flex-direction: column; align-items: center; justify-content: center;
    padding-bottom: 1.8em;
    color: var(--gold-light);
    text-align: center;
    white-space: nowrap;
  }
  .pack--label .brand-banner { top: 1.5em; width: 14.4em; height: 10em; }
  .brand-banner__name { font-size: 2.2em; font-weight: 400; letter-spacing: .04em; line-height: 1.1; }
  .brand-banner__line { font-size: 1.1em; font-weight: 400; letter-spacing: .35em; margin-top: .3em; }

  .product-panel {
    position: absolute; left: 50%; transform: translateX(-50%);
    top: 13.4em; width: 19.8em; height: 15.6em;
    background: var(--panel-black);
    border: .35em solid var(--gold);
    box-shadow: inset 0 0 0 .15em var(--panel-black), inset 0 0 0 .25em var(--gold-light);
    color: var(--ink-light);
    text-align: center;
    padding-top: 1.9em;
    white-space: nowrap;
  }
  .pack--label .product-panel { top: 12.9em; height: 13.9em; padding-top: 1.5em; }

  .product-panel__title { font-size: 1em; font-weight: 300; line-height: 1; }
  .product-panel__title-top { display: block; font-size: 2.8em; letter-spacing: .14em; }
  .product-panel__title-bottom { display: block; margin-top: .1em; line-height: 1; }
  .product-panel__mud { font-size: 2.8em; letter-spacing: .04em; }
  .product-panel__mask { font-size: 3.7em; font-weight: 400; }

  .product-panel__claim { font-family: "Arimo", sans-serif; font-size: 1.15em; letter-spacing: .03em; margin-top: .9em; }
  .product-panel__benefit { font-family: "Kalam", cursive; font-weight: 300; font-size: 1.2em; letter-spacing: .06em; margin-top: .15em; color: var(--ink-soft); }

  .pack__weight {
    position: absolute; left: 0; right: 0; bottom: .5em;
    text-align: center;
    font-family: "Arimo", sans-serif; font-weight: 700; font-size: 1.05em;
    color: var(--ink-dark);
    white-space: nowrap;
  }
  .pack--label .pack__weight { bottom: 1.2em; }
</style>
</head>
<body>

  <section class="pack pack--label" aria-label="Jar label">
    <div class="pack__texture" role="img" aria-label="Distressed gold and white grunge texture"></div>
    <div class="brand-banner">
      <span class="brand-banner__name">Lumen Cove</span>
      <span class="brand-banner__line">SKINCARE</span>
    </div>
    <div class="product-panel">
      <h1 class="product-panel__title">
        <span class="product-panel__title-top">DEAD SEA</span>
        <span class="product-panel__title-bottom"><span class="product-panel__mud">MUD</span> <span class="product-panel__mask">MASK</span></span>
      </h1>
      <p class="product-panel__claim">100% NATURAL - MINERAL RICH</p>
      <p class="product-panel__benefit">Detoxifies and Restores</p>
    </div>
    <p class="pack__weight">250 GRAMS / 8.8 OZ</p>
  </section>

  <section class="pack pack--box" aria-label="Box front">
    <div class="pack__texture" role="img" aria-label="Distressed gold and white grunge texture"></div>
    <div class="brand-banner">
      <span class="brand-banner__name">Lumen Cove</span>
      <span class="brand-banner__line">SKINCARE</span>
    </div>
    <div class="product-panel">
      <h2 class="product-panel__title">
        <span class="product-panel__title-top">DEAD SEA</span>
        <span class="product-panel__title-bottom"><span class="product-panel__mud">MUD</span> <span class="product-panel__mask">MASK</span></span>
      </h2>
      <p class="product-panel__claim">100% NATURAL - MINERAL RICH</p>
      <p class="product-panel__benefit">Detoxifies and Restores</p>
    </div>
    <p class="pack__weight">250 GRAMS / 8.8 OZ</p>
  </section>

</body>
</html>
```